Fantasy Football UX Style Guide & Sample Pages (TKB - not soccer)

Happy April designers!! We are looking to establish a relationship with a killer designer who can work with us on establishing an exciting, professional UX that is delivers a great experience and leverages the powerful technologies of react.js and other 2015 advancements.

Our ideal design team can be one or more people -- but is responsive to feedback, has "no ego" in his/her designs and is willing to go the extra mile to get the job done well. We expect several iterations before any design is considered final. If this excites you - jump in!! If you think working together in an iterative fashion would frustrate you -- please stop now. We will give lots of feedback and ideas. The UX resulting is very important to us.

The site that we are building is related to TKB football. If you have no experience watching American TKB Football -- please stop reading. If you enjoy this game and would like to design UX elements that have an affinity -- please join this design contest.

As a starter project -- we are going to ask that someone review the designs that we have received for a variety of project design competitions. You will notice that they are all pretty disjointed (from our opinion) and also a little 2005 from a design perspective. The winner from this competition will assemble an accepted, killer design that will bring all of these "pages" together into a common design. We would like to see each page in the concept.

Ultimately, what this amounts to is a common style guide that delivers on the strength of the existing brand & logo (files 1 & 2) --- and hopefully -- takes it, and the pages to the next level.

Please note: While our ideal partner will give us an iteration of each page in the new design style guide -- the style guide itself is what is the most important deliverable. We won't expect every page to be perfect. We realize that will take some additional project work.

Target Market(s)

fantasy sports players

Industry/Entity Type

Work

Number of Pages Required

5+ page

Font styles to use
Serif
Sans Serif

Colors
ec1f27
ffffff
161616
959595

Requirements
Must have
• Must Have:
• - A strong sense of brand (please feel free to ask questions; logo is in file 1 & 2)
• - A strong understanding of what resonates with fantasy football players
• - A STYLE GUIDE -- I mention this above but this our primary deliverable for this project. We are looking for an awesome style guide that can be used to deliver any page / mobile app regardless of what is on it. [file attached for example of what a proper style guide looks like. We would like to see this expanded upon]
• - We are looking to see the style guide applied to a variety of page types (examples are shared in the files below -- home page, blog home page, blog item page, specific pages of importance.) This will give us a sense of how the style guide holds up and if we need some new areas addressed in it.
• - We recognize that each page doesn't have to be pixel perfect, and we are willing to take that on as additional project work if the designer would like it.
• - An design that is "easy to read" but conveys excitement
• - We deal with a lot of "sports analytics" so understanding what makes for a good chart is helpful. (if you want to use examples from d3, that is even better)
• - An understanding for how to visualize date & trends in data (see above)
• - A modern REACT.JS like look; not looking for styles from 10 years ago
Nice to have
• - Fresh new takes on the layouts included here.
• - Suggestions for how to make the logo more 2015
• - Creative, visionary ideas
• - Questions for what the screens attached are meant to portray (we'd rather you ask)
Should not have
• - A new logo or color palette. We like what we have and have an established presence here.
• - We are looking for pure, kick-ass design at this point. We don't want it coded.
• - There are many elements that we like from the concept pages below. You don't have to redesign everything. What we don't like is that the UX is not great, and there is no common styling. Also the design itself feels a little "dated" and "dark" in some areas. We are hoping for something more exciting and fresh.

```html
<!DOCTYPE html>
<html lang="en">
<head>
<meta charset="utf-8">
<title>Endzone Oracle — Win Fantasy Football</title>
<link href="https://fonts.googleapis.com/css2?family=Bebas+Neue&family=Oswald:wght@700&family=Roboto:wght@400;500;700&display=swap" rel="stylesheet">
<style>
:root{
  --red:#ec1f27;
  --white:#ffffff;
  --ink:#161616;
  --grey:#959595;
  --text:#222222;
  --muted:#7a7a7a;
  --rule:#e3e3e3;
  --gold:#f2a20c;
}
*{box-sizing:border-box;margin:0;padding:0}
html,body{width:1200px;height:2293px;overflow:hidden;background:var(--white)}
body{position:relative;font-family:'Roboto',sans-serif;color:var(--text)}
.abs{position:absolute}

/* header */
.brand{left:0;top:34px;width:1200px;text-align:center}
.brand-name{display:inline-flex;align-items:center;gap:14px;font-family:'Oswald',sans-serif;font-weight:700;font-size:50px;line-height:1;color:var(--ink);letter-spacing:1px}
.brand-mark{width:64px;height:64px;background:var(--red);display:inline-block}
.brand-tag{font-size:13px;color:#555;margin-top:4px;padding-left:150px}

.nav{left:0;top:130px;width:1200px;height:50px;background:var(--ink);border-bottom:3px solid var(--red)}
.nav-home{position:absolute;left:100px;top:0;width:53px;height:50px;background:var(--red);display:flex;align-items:center;justify-content:center}
.nav-links{position:absolute;left:189px;top:0;height:47px;display:flex;align-items:center;gap:0;list-style:none}
.nav-links li{color:var(--white);font-size:13.5px;font-weight:500;margin-right:42px;text-transform:uppercase}
.nav-tool{position:absolute;top:10px;width:28px;height:28px;background:#333;display:flex;align-items:center;justify-content:center}

/* hero */
.hero{left:100px;top:206px;width:1000px;height:455px;background:linear-gradient(120deg,#2b2e3a 0%,#3c4a6a 40%,#8e99ab 60%,#2a3349 100%)}
.hero-caption{position:absolute;left:0;bottom:0;width:584px;height:83px;background:rgba(22,22,22,.88);padding:16px 16px}
.hero-title{color:var(--white);font-weight:700;font-size:16px;text-transform:uppercase;letter-spacing:.3px}
.hero-text{color:#ddd;font-size:11.5px;line-height:1.5;margin-top:10px;width:540px}
.hero-date{position:absolute;left:584px;bottom:0;width:86px;height:83px;background:var(--red);color:var(--white);text-align:center;padding-top:10px}
.hero-date b{display:block;font-family:'Bebas Neue',sans-serif;font-weight:400;font-size:46px;line-height:1}
.hero-date span{font-size:11px}
.hero-arrows{position:absolute;right:16px;bottom:17px;display:flex;gap:2px}
.hero-arrows div{width:42px;height:39px;background:var(--red);display:flex;align-items:center;justify-content:center}

/* section headings */
.section-head{height:37px;border-bottom:1px solid var(--red)}
.section-head h2{display:inline-block;height:37px;background:var(--red);color:var(--white);font-family:'Bebas Neue',sans-serif;font-weight:400;font-size:26px;line-height:39px;padding:0 15px;letter-spacing:.5px}

/* videos */
.photo{position:absolute;overflow:hidden}
.tag{position:absolute;left:0;top:0;background:var(--red);color:var(--white);font-size:8px;text-transform:uppercase;padding:2px 5px}
.play{position:absolute;left:50%;top:50%;width:34px;height:24px;margin:-12px 0 0 -17px;background:rgba(0,0,0,.65);display:flex;align-items:center;justify-content:center}
.video-title{position:absolute;font-weight:500;font-size:15px;line-height:1.45;color:var(--ink)}
.video-lead .video-title{color:var(--white)}

/* blog */
.blog-title{font-weight:700;font-size:16px;color:var(--ink)}
.blog-text{font-size:12px;line-height:1.6;color:var(--muted);margin-top:9px}
.share-row{display:flex;gap:20px;margin-top:18px}
.share{display:flex;align-items:center;gap:4px}
.share i{font-style:normal;display:inline-block;height:16px;line-height:16px;font-size:8.5px;color:var(--white);padding:0 7px 0 16px;position:relative;border-radius:2px}
.share i::before{content:"";position:absolute;left:4px;top:4px;width:8px;height:8px;background:rgba(255,255,255,.8)}
.share em{font-style:normal;display:inline-block;height:16px;line-height:14px;font-size:8.5px;color:#555;border:1px solid #ccc;padding:0 6px;min-width:22px}
.s-blue i{background:#3c5a97}
.s-sky i{background:#e8eef5;color:#3a6fa8;border:1px solid #9fb9d8}
.s-red i{background:var(--red)}

/* lists */
.item-title{font-size:12px;font-weight:500;line-height:1.6;color:var(--ink)}
.stars{color:var(--gold);font-size:9px;letter-spacing:1px;margin-top:4px}
.stars s{text-decoration:none;color:#ccc}
.date{color:var(--red);font-size:10px;font-weight:500;margin-top:3px}
.item-text{font-size:12px;line-height:1.65;color:var(--muted);margin-top:6px}

/* ad */
.ad{left:171px;top:1913px;width:857px;height:85px;background:linear-gradient(90deg,#050505 0%,#141414 30%,#3b1a08 45%,#b4471a 55%,#1a0f08 70%,#050505 100%);display:flex;align-items:center;justify-content:space-between;padding:0 50px 0 14px}
.ad-name{color:var(--white);font-weight:700;font-size:30px}
.ad-line{color:var(--white);font-family:'Roboto',sans-serif;font-size:27px}

/* footer */
.footer-rule{left:0;top:2038px;width:1200px;height:1px;background:var(--rule)}
.foot h3{font-size:13.5px;font-weight:500;color:#333;text-transform:uppercase}
.foot p{font-size:12.5px;line-height:1.7;color:#555;margin-top:14px}
.divider{width:1px;background:var(--rule);top:2080px;height:148px}
.email{display:flex;gap:12px;margin-top:22px}
.email div{width:180px;height:40px;border:1px solid #ccc;border-radius:2px;font-size:12px;padding:12px 10px;color:#333}
.email b{width:90px;height:40px;background:var(--red);color:var(--white);font-family:'Bebas Neue',sans-serif;font-weight:400;font-size:19px;line-height:42px;text-align:center;border-radius:2px}
.socials{display:flex;gap:9px;margin-top:16px}
.socials span{width:33px;height:33px;display:block}
.bottom{left:0;top:2242px;width:1200px;height:51px;background:var(--ink);color:var(--grey);font-size:12px;display:flex;align-items:center;justify-content:center}
.bottom .code{position:absolute;right:70px;color:var(--white)}
</style>
</head>
<body>

<header class="abs brand">
  <div class="brand-name"><span class="brand-mark"></span>ENDZONE ORACLE</div>
  <div class="brand-tag">Win.Fantasy Football</div>
</header>

<nav class="abs nav">
  <div class="nav-home">
    <svg width="18" height="16" viewBox="0 0 18 16"><path d="M1 8 9 1l8 7M3.5 6.5V15h4v-4h3v4h4V6.5" fill="none" stroke="#fff" stroke-width="1.6"/></svg>
  </div>
  <ul class="nav-links">
    <li>Weekly Rankings</li><li>TKB Teams</li><li>Preseason</li><li>TKB Football</li><li>Latest Article</li><li>Login/Register</li>
  </ul>
  <div class="nav-tool" style="left:1033px"><svg width="12" height="12" viewBox="0 0 12 12"><circle cx="5" cy="5" r="3.5" fill="none" stroke="#fff" stroke-width="1.5"/><path d="M7.7 7.7 11 11" stroke="#fff" stroke-width="1.5"/></svg></div>
  <div class="nav-tool" style="left:1070px"><svg width="14" height="12" viewBox="0 0 14 12"><path d="M1 3h3l5 6h3M1 9h3l5-6h3M10 1l2 2-2 2M10 7l2 2-2 2" fill="none" stroke="#fff" stroke-width="1.3"/></svg></div>
</nav>

<section class="abs hero" role="img" aria-label="Photo of a ball carrier in white evading a defender in black and gold">
  <div class="hero-caption">
    <div class="hero-title">Crane rejected $3M offer from Sharks</div>
    <div class="hero-text">The Sharks offered free agent Marcus Crane “close to $3 million” but he turned it down, according to the Coastal Ledger.</div>
  </div>
  <div class="hero-date"><b>12</b><span>April</span></div>
  <div class="hero-arrows">
    <div><svg width="8" height="12" viewBox="0 0 8 12"><path d="M6 1 1 6l5 5" fill="none" stroke="#fff" stroke-width="1.5"/></svg></div>
    <div><svg width="8" height="12" viewBox="0 0 8 12"><path d="M2 1l5 5-5 5" fill="none" stroke="#fff" stroke-width="1.5"/></svg></div>
  </div>
</section>

<!-- featured video -->
<div class="abs section-head" style="left:100px;top:691px;width:670px"><h2>Featured Video</h2></div>

<div class="video-lead">
  <div class="photo" style="left:100px;top:752px;width:276px;height:230px;background:linear-gradient(160deg,#3a2f5a,#5a4f7a 45%,#2c2c36)" role="img" aria-label="Video still of a player in purple running with the ball">
    <span class="tag">Video</span>
    <span class="play"><svg width="10" height="12" viewBox="0 0 10 12"><path d="M0 0l10 6-10 6z" fill="#fff"/></svg></span>
    <div class="video-title" style="left:26px;top:178px;width:220px">Devon Riley will begin FA visits this week</div>
  </div>
</div>
<div class="photo" style="left:407px;top:752px;width:211px;height:178px;background:linear-gradient(180deg,#4b5a6e,#6b7a6a 55%,#4f7a3c)" role="img" aria-label="Video still of a runner in dark blue being chased on the field">
  <span class="tag">Video</span><span class="play"><svg width="10" height="12" viewBox="0 0 10 12"><path d="M0 0l10 6-10 6z" fill="#fff"/></svg></span>
</div>
<div class="video-title" style="left:407px;top:942px;width:211px">Cougars target 15 carries a game for Stanton</div>
<div class="photo" style="left:650px;top:752px;width:211px;height:178px;background:linear-gradient(180deg,#4a3f2e,#c9c3b2 55%,#6b6048)" role="img" aria-label="Video still of a player in white and gold">
  <span class="tag">Video</span><span class="play"><svg width="10" height="12" viewBox="0 0 10 12"><path d="M0 0l10 6-10 6z" fill="#fff"/></svg></span>
</div>
<div class="video-title" style="left:650px;top:942px;width:211px">Report: Sean Bradley con-templated retirement</div>
<div class="photo" style="left:890px;top:752px;width:210px;height:178px;background:linear-gradient(180deg,#7c8b6a,#2a2a2a 50%,#5f7a3c)" role="img" aria-label="Video still of a player in black carrying the ball">
  <span class="tag">Video</span><span class="play"><svg width="10" height="12" viewBox="0 0 10 12"><path d="M0 0l10 6-10 6z" fill="#fff"/></svg></span>
</div>
<div class="video-title" style="left:890px;top:942px;width:210px">Report: Sean Bradley con-templated retirement</div>

<!-- latest blog news -->
<div class="abs section-head" style="left:100px;top:1026px;width:1000px"><h2>Latest Blog News</h2></div>

<article class="abs" style="left:100px;top:1092px;width:318px">
  <div class="photo" style="position:relative;width:318px;height:179px;background:linear-gradient(180deg,#4b5a6e,#6b7a6a 55%,#4f7a3c)" role="img" aria-label="Photo of a runner breaking away from defenders"><span class="tag">Fantasy Football</span></div>
  <h3 class="blog-title" style="margin-top:15px">Hawks do 1-yr, $2.3M deal with Myles Aston</h3>
  <p class="blog-text">Hawks agreed to terms with WR Myles Aston, formerly of the Bisons, on a one-year, $2.3 million contract.</p>
  <div class="share-row"><span class="share s-blue"><i>Share</i><em>33</em></span><span class="share s-sky"><i>Post</i><em>4</em></span><span class="share s-red"><i>Share</i><em>0</em></span></div>
</article>
<article class="abs" style="left:440px;top:1092px;width:319px">
  <div class="photo" style="position:relative;width:319px;height:179px;background:linear-gradient(120deg,#2b2e3a,#3c4a6a 40%,#8e99ab 60%,#2a3349)" role="img" aria-label="Photo of a ball carrier in white evading a defender in black"><span class="tag">Fantasy Football</span></div>
  <h3 class="blog-title" style="margin-top:15px">Hawks do 1-yr, $2.3M deal with Myles Aston</h3>
  <p class="blog-text">Hawks agreed to terms with WR Myles Aston, formerly of the Bisons, on a one-year, $2.3 million contract.</p>
  <div class="share-row"><span class="share s-blue"><i>Share</i><em>33</em></span><span class="share s-sky"><i>Post</i><em>4</em></span><span class="share s-red"><i>Share</i><em>0</em></span></div>
</article>
<article class="abs" style="left:781px;top:1092px;width:319px">
  <div class="photo" style="position:relative;width:319px;height:179px;background:linear-gradient(180deg,#7c8b6a,#2a2a2a 50%,#5f7a3c)" role="img" aria-label="Photo of a player in black carrying the ball"><span class="tag">Fantasy Football</span></div>
  <h3 class="blog-title" style="margin-top:15px">Hawks do 1-yr, $2.3M deal with Myles Aston</h3>
  <p class="blog-text">Hawks agreed to terms with WR Myles Aston, formerly of the Bisons, on a one-year, $2.3 million contract.</p>
  <div class="share-row"><span class="share s-blue"><i>Share</i><em>33</em></span><span class="share s-sky"><i>Post</i><em>4</em></span><span class="share s-red"><i>Share</i><em>0</em></span></div>
</article>

<!-- player news -->
<div class="abs section-head" style="left:100px;top:1442px;width:545px"><h2>Player News</h2></div>
<div class="abs section-head" style="left:716px;top:1442px;width:379px"><h2>Football 2015</h2></div>

<div class="abs" style="left:100px;top:1517px">
  <div class="photo" style="left:0;top:0;width:92px;height:83px;background:linear-gradient(180deg,#4b5a6e,#4f7a3c)" role="img" aria-label="Thumbnail of a runner on the field"></div>
  <div class="abs" style="left:105px;top:0;width:165px"><div class="item-title">Report: Sean Bradley conm plated retirement</div><div class="stars">★★★<s>★★</s></div><div class="date">12 MARCH 2013</div></div>
  <div class="photo" style="left:291px;top:0;width:92px;height:83px;background:linear-gradient(180deg,#6a6a6a,#a33030 50%,#4f7a3c)" role="img" aria-label="Thumbnail of a player in red"></div>
  <div class="abs" style="left:396px;top:0;width:165px"><div class="item-title">Report: Sean Bradley conm plated retirement</div><div class="stars">★★★<s>★★</s></div><div class="date">12 MARCH 2013</div></div>

  <div class="photo" style="left:0;top:121px;width:92px;height:83px;background:linear-gradient(180deg,#4a3f2e,#c9c3b2 60%,#6b6048)" role="img" aria-label="Thumbnail of a player in white and gold"></div>
  <div class="abs" style="left:105px;top:121px;width:165px"><div class="item-title">Report: Sean Bradley conm plated retirement</div><div class="stars">★★★<s>★★</s></div><div class="date">12 MARCH 2013</div></div>
  <div class="photo" style="left:291px;top:121px;width:92px;height:83px;background:linear-gradient(180deg,#555,#b8b8c8 50%,#8a2a3a)" role="img" aria-label="Thumbnail of a player in white and maroon"></div>
  <div class="abs" style="left:396px;top:121px;width:165px"><div class="item-title">Report: Sean Bradley conm plated retirement</div><div class="stars">★★★<s>★★</s></div><div class="date">12 MARCH 2013</div></div>

  <div class="photo" style="left:0;top:241px;width:92px;height:83px;background:linear-gradient(120deg,#2b2e3a,#8e99ab 55%,#2a3349)" role="img" aria-label="Thumbnail of a tackle in progress"></div>
  <div class="abs" style="left:105px;top:241px;width:165px"><div class="item-title">Report: Sean Bradley conm plated retirement</div><div class="stars">★★★<s>★★</s></div><div class="date">12 MARCH 2013</div></div>
  <div class="photo" style="left:291px;top:241px;width:92px;height:83px;background:linear-gradient(180deg,#4a3f2e,#c9c3b2 60%,#6b6048)" role="img" aria-label="Thumbnail of a quarterback in white"></div>
  <div class="abs" style="left:396px;top:241px;width:165px"><div class="item-title">Report: Sean Bradley conm plated retirement</div><div class="stars">★★★<s>★★</s></div><div class="date">12 MARCH 2013</div></div>
</div>

<div class="abs" style="left:716px;top:1515px;width:384px">
  <div class="photo" style="left:0;top:0;width:178px;height:147px;background:linear-gradient(120deg,#2b2e3a,#3c4a6a 40%,#8e99ab 60%,#2a3349)" role="img" aria-label="Photo of a ball carrier in white evading a defender"></div>
  <div class="abs" style="left:191px;top:0;width:190px"><div class="item-title">Report: Sean Bradley conm plated retirement</div><div class="item-text">Hawks agreed to terms with WR Myles Aston, formerly of the Bisons, on a one-year, $2.3 million</div><div class="stars">★★★<s>★★</s></div><div class="date">12 MARCH 2013</div></div>
  <div class="photo" style="left:0;top:179px;width:178px;height:147px;background:linear-gradient(160deg,#6a7a8a,#1f3a8a 50%,#2a2f4a)" role="img" aria-label="Photo of a receiver in blue holding the ball"></div>
  <div class="abs" style="left:191px;top:179px;width:190px"><div class="item-title">Report: Sean Bradley conm plated retirement</div><div class="item-text">Hawks agreed to terms with WR Myles Aston, formerly of the Bisons, on a one-year, $2.3 million</div><div class="stars">★★★<s>★★</s></div><div class="date">12 MARCH 2013</div></div>
</div>

<!-- ad -->
<div class="abs ad" role="img" aria-label="Advertising banner for Bright Frame Studio">
  <span class="ad-name">Bright Frame Studio</span>
  <span class="ad-line">At the Convergence of Art &amp; Technology</span>
</div>

<!-- footer -->
<div class="abs footer-rule"></div>
<div class="abs foot" style="left:100px;top:2080px;width:280px">
  <h3>Connect With Us</h3>
  <p>Register for diabetes news, research and food &amp; fitness tips. - See more at:</p>
  <div class="email"><div>Email:</div><b>SIGN UP</b></div>
</div>
<div class="abs divider" style="left:405px"></div>
<div class="abs foot" style="left:451px;top:2080px;width:250px">
  <h3 style="text-transform:none">FIND US ON</h3>
  <div class="socials" aria-label="Social profiles">
    <span style="background:#2d4a86"></span><span style="background:#2a8ad8"></span><span style="background:#c8232c"></span><span style="background:#d9352a"></span><span style="background:#5a4a3a"></span><span style="background:#f26522"></span>
  </div>
</div>
<div class="abs divider" style="left:722px"></div>
<div class="abs foot" style="left:760px;top:2080px;width:170px">
  <h3>Services</h3>
  <p style="padding-left:3px">But I must explain to you how all this mistaken idea of denouncing pleasure and praising pain was born aneso one rejects.</p>
</div>
<div class="abs divider" style="left:933px"></div>
<div class="abs foot" style="left:978px;top:2080px;width:150px">
  <h3>Other Links</h3>
  <p>But I must explain to how all this mistaken idof denouncing pleasureaisi ng pain was born anesr</p>
</div>

<footer class="abs bottom">
  © 2015 Endzone Oracle.com &nbsp;-&nbsp; Advertise &nbsp;-&nbsp; Terms &nbsp;-&nbsp; Feedback &nbsp;Links
  <span class="code">C4</span>
</footer>

</body>
</html>
```